Marwick Ostrand Law website for a law firm

modern clean website for a small boutique law firm. Based in Sacramento, CA and the Bay Area. Practice areas of Family Law, Civil litigation, and Criminal Defense. We already have a logo design as well as attorney pictures to include on page.
Would like images of California included on site.
Would like site to go with Logo that is already designed...blue/grey/white colors.

Industry/Entity Type

Law Firm

Number of Pages Required

5+ page

Requirements
Must have
• I already have several pages of content drafted. Just need the pages with images to input content. Must be clean and modern feel. Want it to reflect California and small boutique feel that is provided personalized legal attention.
• Must have a page where I can blog or post articles on.

```html
<!DOCTYPE html>
<html lang="en">
<head>
<meta charset="utf-8">
<title>Marwick Ostrand Law</title>
<link href="https://fonts.googleapis.com/css2?family=Cabin:wght@400;500;600;700&family=Josefin+Sans:wght@300;400&family=Libre+Baskerville:ital,wght@1,700&display=swap" rel="stylesheet">
<style>
:root{
  --ink:#111111;
  --bar:#0a0a0a;
  --blue:#3f86c8;
  --grey-text:#666666;
  --panel:#f1f1f1;
  --white:#ffffff;
  --footer:#161616;
  --footer-text:#9a9a9a;
  --brick:#9a5a3e;
  --brick-dark:#4a2c22;
  --suit:#2a2d34;
  --sky:#78b3e6;
}
*{box-sizing:border-box;margin:0;padding:0}
html,body{width:687px;height:1200px;overflow:hidden;background:var(--white)}
body{position:relative;font-family:"Josefin Sans",sans-serif;color:var(--ink)}
.topbar{position:absolute;left:0;top:0;width:687px;height:24px;background:var(--bar);color:var(--white);font-size:9px;display:flex;justify-content:flex-end;align-items:center;padding-right:46px;gap:10px}
.topbar span{display:flex;align-items:center;gap:5px}
.topbar .divider{width:1px;height:14px;background:#888}
.header{position:absolute;left:0;top:24px;width:687px;height:48px;background:var(--white)}
.brand{position:absolute;left:44px;top:10px;font-family:"Josefin Sans",sans-serif;font-weight:300;font-size:30px;letter-spacing:0;color:var(--blue);line-height:1;white-space:nowrap}
.nav{position:absolute;right:44px;top:0;display:flex;gap:40px;height:48px;align-items:center;font-size:10px;color:#333}
.nav a{color:inherit;text-decoration:none;position:relative;height:48px;line-height:50px}
.nav a.active{color:var(--ink)}
.nav a.active::before{content:"";position:absolute;left:-8px;right:-8px;top:0;height:3px;background:var(--blue)}
.hero{position:absolute;left:0;top:72px;width:687px;height:328px;
  background:
    radial-gradient(ellipse 120px 180px at 150px 230px,rgba(60,64,80,.85),rgba(60,64,80,0)),
    radial-gradient(ellipse 120px 190px at 300px 240px,rgba(30,32,40,.9),rgba(30,32,40,0)),
    radial-gradient(ellipse 140px 120px at 40px 60px,rgba(190,170,90,.55),rgba(190,170,90,0)),
    linear-gradient(180deg,rgba(0,0,0,0) 60%,rgba(40,25,20,.45)),
    linear-gradient(100deg,#7a4e36 0%,var(--brick) 25%,#a9674a 45%,#8c5038 65%,var(--brick-dark) 100%)}
.hero-title{position:absolute;right:44px;top:94px;font-family:"Josefin Sans",sans-serif;font-weight:300;font-size:50px;color:var(--white);line-height:1;white-space:nowrap}
.hero-tag{position:absolute;right:45px;top:163px;font-family:"Libre Baskerville",serif;font-style:italic;font-weight:700;font-size:9.5px;color:var(--white);letter-spacing:.2px;white-space:nowrap}
.btn-light{position:absolute;right:45px;top:186px;width:148px;height:36px;background:var(--white);border-radius:3px;font-family:"Josefin Sans",sans-serif;font-size:12.5px;color:var(--ink);display:flex;align-items:center;justify-content:center;box-shadow:0 2px 4px rgba(0,0,0,.3)}
.section-title{position:absolute;left:0;width:687px;text-align:center;font-family:"Cabin",sans-serif;font-weight:700;font-size:22px;letter-spacing:.5px}
.section-title em{font-style:normal;color:var(--blue)}
.practice{position:absolute;top:467px;width:180px;height:163px}
.practice .photo{position:absolute;left:0;top:0;width:180px;height:120px}
.practice .label{position:absolute;left:0;top:130px;width:180px;text-align:center;font-family:"Cabin",sans-serif;font-weight:500;font-size:13px}
.practice.featured{width:190px;height:163px;left:44px;background:var(--panel);box-shadow:0 0 4px rgba(0,0,0,.25)}
.practice.featured .photo{left:5px;top:4px}
.practice.featured .label{width:190px;color:var(--blue)}
.welcome{position:absolute;left:0;top:661px;width:687px;height:180px;
  background:
    linear-gradient(90deg,rgba(255,255,255,0) 10%,rgba(255,255,255,.35) 15%,rgba(255,255,255,0) 20%,rgba(255,255,255,0) 80%,rgba(255,255,255,.35) 86%,rgba(255,255,255,0) 92%),
    linear-gradient(180deg,#efe8e4,#f3eeea 60%,#ebe3de)}
.welcome h2{position:absolute;top:30px}
.welcome p{position:absolute;left:80px;top:65px;width:527px;text-align:center;font-size:8.2px;line-height:15.2px;color:#444}
.btn-blue{position:absolute;height:30px;width:120px;background:var(--blue);color:var(--white);font-family:"Josefin Sans",sans-serif;font-size:11.5px;display:flex;align-items:center;justify-content:center;border-radius:2px;box-shadow:0 2px 3px rgba(0,0,0,.3)}
.member{position:absolute;top:909px;width:292px;height:161px;background:var(--panel)}
.member .photo{position:absolute;left:0;top:0;width:131px;height:161px}
.member h3{position:absolute;left:146px;top:16px;font-family:"Cabin",sans-serif;font-weight:500;font-size:13.5px}
.member p{position:absolute;left:146px;top:42px;width:138px;font-size:7.9px;line-height:13.2px;color:var(--grey-text)}
.member .btn-blue{left:146px;top:113px}
.footer{position:absolute;left:0;top:1105px;width:687px;height:95px;background:var(--footer)}
.footer .brand{top:30px;font-size:30px}
.footer-nav{position:absolute;left:211px;top:28px;display:flex;gap:21px;font-size:7px;color:var(--footer-text);letter-spacing:.3px}
.footer-nav .current{color:var(--blue)}
.footer-rule{position:absolute;left:184px;top:47px;width:320px;height:1px;background:#3a3a3a}
.copyright{position:absolute;left:0;width:687px;top:66px;text-align:center;font-size:8px;color:#ccc}
.copyright b{color:var(--blue);font-weight:400;font-size:10px}
.social{position:absolute;right:44px;top:41px;display:flex;gap:6px}
.social span{width:18px;height:18px;border-radius:50%;background:#d8d8d8;display:block}
</style>
</head>
<body>
<div class="topbar">
  <span><svg width="11" height="8" viewBox="0 0 11 8"><rect x=".5" y=".5" width="10" height="7" fill="none" stroke="#3f86c8"/><path d="M.5 .5 5.5 4.5 10.5 .5" fill="none" stroke="#3f86c8"/></svg>info@marwickostrand.com</span>
  <i class="divider"></i>
  <span><svg width="9" height="9" viewBox="0 0 24 24"><path fill="#3f86c8" d="M6.6 10.8a15 15 0 0 0 6.6 6.6l2.2-2.2a1 1 0 0 1 1-.25 11.4 11.4 0 0 0 3.6.57 1 1 0 0 1 1 1V20a1 1 0 0 1-1 1A17 17 0 0 1 3 4a1 1 0 0 1 1-1h3.5a1 1 0 0 1 1 1c0 1.25.2 2.45.57 3.57a1 1 0 0 1-.25 1z"/></svg>(925) 555-0142</span>
</div>

<header class="header">
  <div class="brand">MO LAW</div>
  <nav class="nav">
    <a class="active">Home</a><a>About Us</a><a>Practice Areas</a><a>Contact Us</a>
  </nav>
</header>

<section class="hero" role="img" aria-label="Photo of the two founding attorneys standing in front of a red brick California office building">
  <div class="hero-title">MO LAW</div>
  <div class="hero-tag">STRONG REPUTATIONS DON'T GO UNNOTICED</div>
  <div class="btn-light">GET APPOINTMENT</div>
</section>

<h2 class="section-title" style="top:428px">PRACTICE <em>AREAS</em></h2>

<div class="practice featured">
  <div class="photo" role="img" aria-label="Business meeting with documents on a table" style="background:radial-gradient(ellipse 70px 40px at 95px 65px,#4a4a4a,rgba(74,74,74,0)),linear-gradient(135deg,#2c2c2c,#131313 55%,#333)">
    <svg width="180" height="120"><path d="M90 52v16M82 60h16" stroke="#fff" stroke-width="1.5"/></svg>
  </div>
  <div class="label">Business Law</div>
</div>
<div class="practice" style="left:253px">
  <div class="photo" role="img" aria-label="Smiling family outdoors under a blue California sky" style="background:radial-gradient(ellipse 80px 55px at 95px 75px,rgba(220,190,170,.8),rgba(220,190,170,0)),linear-gradient(180deg,var(--sky),#a9cff0 55%,#6f9aa8)"></div>
  <div class="label">Family Law</div>
</div>
<div class="practice" style="left:460px">
  <div class="photo" role="img" aria-label="Hands resting through prison cell bars" style="background:radial-gradient(ellipse 60px 35px at 110px 55px,rgba(190,150,120,.75),rgba(190,150,120,0)),linear-gradient(90deg,#2a302b,#5c6256 40%,#8a8a7c 60%,#343933)"></div>
  <div class="label">Criminal Defense</div>
</div>

<section class="welcome" role="img" aria-label="Faded conference room background">
  <h2 class="section-title">WELCOME TO <em>MO LAW</em></h2>
  <p>After practicing in both the private and public sector for several years, Clara Marwick and Devin Ostrand joined their legal expertise and formed Marwick &amp; Ostrand Law in 2015. With a combined 15 years of experience, Clara and Devin specialize in Civil Litigation, Family Law, Immigration and Criminal Defense. Their goal is to provide their clients with the best possible outcome in each and every case.</p>
  <div class="btn-blue" style="left:283px;top:121px">LEARN MORE</div>
</section>

<h2 class="section-title" style="top:870px">OUR <em>TEAM</em></h2>

<article class="member" style="left:44px">
  <div class="photo" role="img" aria-label="Portrait of attorney Clara R. Marwick in front of a blue abstract painting" style="background:radial-gradient(ellipse 45px 80px at 70px 110px,rgba(45,45,60,.9),rgba(45,45,60,0)),linear-gradient(160deg,#2f5e88,#b9c8d4 40%,#3e6e96 70%,#2a2f3c)"></div>
  <h3>Clara R. Marwick</h3>
  <p>Clara Marwick founder and partner, is a California native who grew up in the same community she serves.Clara is a graduate of Valley State University.</p>
  <div class="btn-blue">READ MORE</div>
</article>
<article class="member" style="left:350px">
  <div class="photo" role="img" aria-label="Portrait of attorney Devin A. Ostrand seated with a document" style="background:radial-gradient(ellipse 50px 70px at 70px 120px,rgba(20,22,30,.95),rgba(20,22,30,0)),linear-gradient(90deg,#8f7c68,#b09a82 30%,#6e5a4c 70%,#8a6d58)"></div>
  <h3>Devin A. Ostrand</h3>
  <p>Devin Ostrand is a founding partner of Marwick &amp; Ostrand Law. After years of helping clients at other local civil litigation law firms, he started this firm.</p>
  <div class="btn-blue">READ MORE</div>
</article>

<footer class="footer">
  <div class="brand">MO LAW</div>
  <nav class="footer-nav"><span class="current">HOME</span><span>ABOUT US</span><span>PRACTICE AREAS</span><span>TEAM</span><span>CONTACT US</span></nav>
  <div class="footer-rule"></div>
  <div class="copyright">© <b>MO LAW</b> - 2017. All Rights reserved.</div>
  <div class="social"><span></span><span></span><span></span><span></span></div>
</footer>
</body>
</html>
```